1/2 Page B&W Ad for Conference Program

Hi:

We are an industrial and environmental engineering firm in Seattle. We we design facilities and the internal process technologies for advanced renewable energy projects such as biofuels, waste to energy and other biomass to heat, power, steam, fuel or chemical projects.

We are attending www.verdantfuelsummit.net this month in Toronto. Our package allows to a 1/2 page ad in the conference book.

The specs for the half page BLACK & WHITE ad are: max width: 7.5 inches, max height: 3.5 inches (no bleeds). Any common high resolution format may be provided (EPS, PDF, etc.)

----

K7 Power Associates
www.k7powerassociates.net
+1 (206) 555-0147
Seattle, WA USA

I wish to convey that we are an "industrial engineering firm specializing in advanced renewable energy projects worldwide".

The services we wish to profile are:

* FEED Front End Engineering Design
* Process Engineering, Design & Scale-Up
* Technical Feasibility & Investor Due Diligence Studies
* Project Management

Registered Professional Engineers in the U.S. & Canada. (Maybe in smaller text).

Our logo is attached. I have included a B&W logo but would prefer a cleaner look. Otherwise, feel free to use stock images of industrial scale (oil refinery, power plant, chemical plant, etc) blended with renewable imaging (biodiesel, etc.). We try to stay away from "green washing" such as two hands holding a plant, children playing in a grass field, etc.

Our image is that of industrial professionals working the advanced renewable energy industry.

The ad should show our logo + the contact address above.

We also need a new website but that project is next...

I need to submit the artwork to the conference by end of day Friday, May 8.

Feel free to ask questions! Thanks!!

Dale Morrowfield

Target Market(s)

Project developers and investors planning to invest 30M+ $ in designing and building an advanced renewable energy (biodiesel,etc. ) project. Also, private equity firms needing an engineering firm to help them evaluate projects to fund. Technical feasibility studies.

Industry/Entity Type

Industrial

Font styles to use
Sans Serif

Requirements
Nice to have
• Scandinavian style design.
Should not have
• Cheesy "green energy" ads. The industry today is large scale, industrial and serious about profitability - but also embracing new technologies and moving energy in a cleaner direction.
• Cannot use the Image of Vostrand that is uploaded. But this is our project and an example of an industrial scale biodiesel plant.

```html
<!DOCTYPE html>
<html lang="en">
<head>
<meta charset="utf-8">
<title>K7 Power Associates – Half Page Ad</title>
<link rel="stylesheet" href="https://fonts.googleapis.com/css2?family=Open+Sans:ital,wght@0,400;0,700;0,800;1,400;1,700&display=swap">
<style>
  :root {
    --page-bg: #e9e9e6;
    --ad-bg: #ffffff;
    --ink: #111111;
    --ink-soft: #555555;
    --band: #b5b5b5;
    --photo-top: #d9d9d9;
    --photo-mid: #c4c4c4;
    --photo-low: #9a9a9a;
  }
  * { margin: 0; padding: 0; box-sizing: border-box; }
  html, body {
    width: 1200px;
    height: 1031px;
    overflow: hidden;
    background: var(--page-bg);
    font-family: "Open Sans", Arial, sans-serif;
    color: var(--ink);
  }
  .ad {
    position: absolute;
    left: 50px;
    top: 260px;
    width: 1100px;
    height: 510px;
    background: var(--ad-bg);
    overflow: hidden;
    box-shadow: 0 2px 10px rgba(0,0,0,0.12);
  }
  .ad-art {
    position: absolute;
    inset: 0;
    width: 1100px;
    height: 510px;
  }
  .ad-copy {
    position: absolute;
    left: 597px;
    top: 30px;
    width: 480px;
  }
  .headline {
    font-weight: 800;
    font-size: 22px;
    line-height: 1.24;
    letter-spacing: 2px;
    text-transform: uppercase;
    text-align: left;
  }
  .services {
    list-style: none;
    margin-top: 30px;
    font-size: 17px;
    line-height: 1.42;
    color: var(--ink-soft);
  }
  .services li::before { content: "• "; }
  .registration {
    margin-top: 16px;
    font-size: 14px;
    font-style: italic;
    color: var(--ink);
  }
  .registration strong { font-weight: 700; }
  .brand {
    position: absolute;
    left: 600px;
    top: 372px;
    display: flex;
    align-items: center;
    gap: 12px;
  }
  .brand-dot {
    width: 34px;
    height: 34px;
    border-radius: 50%;
    background: var(--ink);
  }
  .brand-name {
    font-weight: 800;
    font-size: 32px;
    letter-spacing: 0.3px;
    color: var(--ink);
  }
  .contact {
    position: absolute;
    right: 22px;
    bottom: 8px;
    font-size: 16px;
    color: var(--ink);
  }
  .contact span { margin-left: 12px; }
</style>
</head>
<body>
  <section class="ad">
    <svg class="ad-art" viewBox="0 0 1100 510">
      <defs>
        <linearGradient id="plantTones" x1="0" y1="0" x2="0" y2="1">
          <stop offset="0%" stop-color="var(--photo-top)"/>
          <stop offset="55%" stop-color="var(--photo-mid)"/>
          <stop offset="100%" stop-color="var(--photo-low)"/>
        </linearGradient>
      </defs>
      <path class="contact-band" d="M390 510 C420 486 440 474 480 474 L1100 474 L1100 510 Z" fill="var(--band)"/>
      <circle class="plant-photo" cx="268" cy="282" r="222" fill="url(#plantTones)" role="img" aria-label="Black and white photograph of a large industrial biodiesel plant with storage tanks and steel walkways"/>
    </svg>

    <div class="ad-copy">
      <h1 class="headline">Industrial engineering firm<br>specializing in advanced<br>renewable energy projects<br>worldwide</h1>
      <ul class="services">
        <li>FEED Front End Engineering Design</li>
        <li>Process Engineering, Design &amp; Scale-Up</li>
        <li>Technical Feasibility &amp; Investor Due Diligence Studies</li>
        <li>Project Management</li>
      </ul>
      <p class="registration"><strong>Registered Professional Engineers</strong> in the <strong>U.S.</strong> &amp; <strong>Canada</strong></p>
    </div>

    <div class="brand">
      <div class="brand-dot"></div>
      <div class="brand-name">K7 Power Associates</div>
    </div>

    <p class="contact">+1 (206) 555-0147<span>Seattle, WA USA</span><span>www.k7powerassociates.net</span></p>
  </section>
</body>
</html>
```